Financial services firm needs updated web design

Our current website, coinpathwealth.example was created by ourselves using templates provided by our website host, Harborline Webworks. We are looking to get a whole new look and feel to our website that is clean, professional and easy to navigate. The design must be able to be transferred to Harborline Webworks for hosting (FTP??-outside my area of expertise - sorry) and that the information can be updated and changed by ourselves in the future. I have included our updated logo and our business card design.
Updates
Project Deadline Extended
Reason: Went away on vacation for two weeks.
Target Market(s)
Age 50+ individuals looking for investment, retirement and estate planning guidance.
Industry/Entity Type
Financial
Number of Pages Required
1 page
Font styles to use
Other font styles liked:
- Adobe Caslon Pro
Look and feel
Each slider illustrates characteristics of the customer's brand and the style your logo design should communicate.

```html
<!DOCTYPE html>
<html lang="en">
<head>
<meta charset="utf-8">
<title>Coinpath Financial Services</title>
<link rel="stylesheet" href="https://fonts.googleapis.com/css2?family=Open+Sans:wght@300;400;600;700;800&display=swap">
<style>
  :root {
    --orange: #ff9000;
    --orange-deep: #ff8a00;
    --orange-glow: #ffb300;
    --nav-active: #ff7e00;
    --header-bg: #ffffff;
    --header-rule: #e6e6e6;
    --brand-text: #6a6a6a;
    --nav-text: #9a9a9a;
    --white: #ffffff;
    --panel-dark: #666666;
    --panel-light: #ebebeb;
    --panel-border: #cfcfcf;
    --page-bg: #f8f8f8;
    --body-text: #555555;
    --accent-text: #ff6a00;
  }
  * { box-sizing: border-box; margin: 0; padding: 0; }
  html, body {
    width: 1200px; height: 579px; overflow: hidden;
    background: var(--page-bg);
    font-family: "Open Sans", Arial, sans-serif;
  }
  .canvas { position: relative; width: 1200px; height: 579px; overflow: hidden; background: var(--page-bg); }

  .site-header {
    position: absolute; left: 0; top: 0; width: 1200px; height: 60px;
    background: var(--header-bg); border-bottom: 1px solid var(--header-rule);
  }
  .brand { position: absolute; left: 182px; top: 0; height: 60px; display: flex; align-items: center; gap: 20px; }
  .brand-dot { width: 14px; height: 14px; border-radius: 50%; background: var(--brand-text); }
  .brand-name { font-size: 18px; font-weight: 400; color: var(--brand-text); letter-spacing: 0.2px; }

  .main-nav { position: absolute; top: 0; right: 182px; height: 43px; display: flex; align-items: center; }
  .main-nav a {
    display: block; text-decoration: none; font-size: 12.5px; color: var(--nav-text);
    padding: 0 15px; line-height: 43px; height: 43px;
  }
  .main-nav a.is-active { background: var(--nav-active); color: var(--white); border-radius: 0 0 4px 4px; padding: 0 13px; }

  .hero {
    position: absolute; left: 0; top: 60px; width: 1200px; height: 443px;
    background: radial-gradient(ellipse 520px 360px at 840px 400px, var(--orange-glow) 0%, var(--orange) 55%, var(--orange-deep) 100%);
  }

  .intro-panel {
    position: absolute; left: 182px; top: 452px; width: 836px; height: 140px;
    background: var(--panel-light); border: 1px solid var(--panel-border); border-radius: 7px 7px 0 0;
    overflow: hidden;
  }
  .intro-panel::before {
    content: ""; position: absolute; left: 0; top: 0; width: 100%; height: 51px; background: var(--panel-dark);
  }
  .intro-text {
    position: absolute; left: 0; top: 72px; width: 100%; text-align: center;
    font-size: 26.5px; font-weight: 300; line-height: 33px; color: var(--body-text); padding: 0 50px;
  }
  .intro-text .accent { color: var(--accent-text); }

  .hero-photo {
    position: absolute; left: 236px; top: 84px; width: 378px; height: 419px;
    border-radius: 150px 150px 40px 40px;
    background: linear-gradient(180deg, #9a5a3a 0%, #e2b397 45%, #caa088 75%, #7a4e38 100%);
  }

  .services { position: absolute; left: 623px; top: 112px; color: var(--white); }
  .services-title { font-size: 32px; font-weight: 800; line-height: 42px; text-shadow: 0 1px 2px rgba(0,0,0,0.2); }
  .services-list { list-style: none; margin-top: 12px; }
  .services-list li {
    display: flex; align-items: center; gap: 9px; font-size: 16.5px; line-height: 30.3px;
    text-shadow: 0 1px 2px rgba(0,0,0,0.2);
  }
  .services-list svg { width: 15px; height: 15px; flex: none; }
  .read-more {
    display: inline-block; margin-top: 10px; padding: 0 9px; height: 32px; line-height: 32px;
    font-size: 13px; color: #222; background: linear-gradient(#ffffff, #e6e6e6);
    border: 1px solid #d0d0d0; border-radius: 4px; text-decoration: none;
    box-shadow: 0 1px 3px rgba(0,0,0,0.25);
  }
</style>
</head>
<body>
<div class="canvas">
  <header class="site-header">
    <div class="brand">
      <span class="brand-dot"></span>
      <span class="brand-name">Coinpath Financial Services</span>
    </div>
    <nav class="main-nav">
      <a href="#" class="is-active">Home</a>
      <a href="#">Our team</a>
      <a href="#">Connect</a>
      <a href="#">Blog</a>
      <a href="#">Contact</a>
    </nav>
  </header>

  <section class="hero">
    <div class="services">
      <h1 class="services-title">Services</h1>
      <ul class="services-list">
        <li><svg viewBox="0 0 16 16"><circle cx="8" cy="8" r="8" fill="#fff"/><path d="M6.5 4.5 10 8l-3.5 3.5" fill="none" stroke="#ff8a00" stroke-width="2"/></svg>Your investment partner</li>
        <li><svg viewBox="0 0 16 16"><circle cx="8" cy="8" r="8" fill="#fff"/><path d="M6.5 4.5 10 8l-3.5 3.5" fill="none" stroke="#ff8a00" stroke-width="2"/></svg>Tax &amp; Estate Planning</li>
        <li><svg viewBox="0 0 16 16"><circle cx="8" cy="8" r="8" fill="#fff"/><path d="M6.5 4.5 10 8l-3.5 3.5" fill="none" stroke="#ff8a00" stroke-width="2"/></svg>Planning tips</li>
        <li><svg viewBox="0 0 16 16"><circle cx="8" cy="8" r="8" fill="#fff"/><path d="M6.5 4.5 10 8l-3.5 3.5" fill="none" stroke="#ff8a00" stroke-width="2"/></svg>Dozens of ideas</li>
      </ul>
      <a href="#" class="read-more">Read More</a>
    </div>
  </section>

  <section class="intro-panel">
    <p class="intro-text">Welcome to <span class="accent">Coinpath Financial Services</span>, Individual Financial Planning, Business Planning Services - Employee Group Benefits</p>
  </section>

  <div class="hero-photo" role="img" aria-label="Photo of a surprised young woman with long hair, hands on her cheeks"></div>
</div>
</body>
</html>
```